Poster Design Needed for Events

I would like a poster designed for our events.. We do evenings of Mediumship/Psychic at theatres ect.. the image below would need to be included... I Would also like the following wording to be included... "Renowned Spiritualist Medium Dewi Carlow Presents Whispers From The Lantern" There will also Need to be a Place on the poster where event details can be put.. as they Change everytime.. Colours for background maybe blue,, maybe Clouds ect..

```html
<!DOCTYPE html>
<html lang="en">
<head>
<meta charset="utf-8">
<title>Dewi Carlow — Whispers From The Lantern</title>
<link href="https://fonts.googleapis.com/css2?family=Montserrat:wght@300;800;900&family=Cinzel:wght@600&family=Josefin+Sans:wght@300&display=swap" rel="stylesheet">
<style>
  :root {
    --sky-top: #f4f8fa;
    --sky-mid: #d6e6ec;
    --sea-low: #5f9aa6;
    --deep-teal: #0f3440;
    --slate: #4b5565;
    --steel-light: #9aa3ab;
    --steel-dark: #4a5259;
    --ornament-blue: 74, 114, 232;
    --text-light: #f2f6f8;
  }
  * { margin: 0; padding: 0; box-sizing: border-box; }
  html, body { width: 934px; height: 1200px; overflow: hidden; background: var(--sky-top); }
  .poster {
    position: relative;
    width: 934px;
    height: 1200px;
    overflow: hidden;
    background: linear-gradient(180deg, var(--sky-top) 0%, var(--sky-mid) 45%, #a9c9d1 68%, var(--sea-low) 80%, var(--deep-teal) 100%);
    font-family: "Josefin Sans", sans-serif;
    color: var(--text-light);
  }
  .cloud-light {
    position: absolute;
    inset: 0;
    background:
      radial-gradient(ellipse 260px 200px at 60px 330px, rgba(255,255,255,.7), transparent 70%),
      radial-gradient(ellipse 260px 200px at 880px 330px, rgba(255,255,255,.7), transparent 70%),
      radial-gradient(ellipse 320px 420px at 480px 240px, rgba(255,255,255,.85), transparent 70%);
  }
  .portrait {
    position: absolute;
    left: 304px;
    top: 208px;
    width: 544px;
    height: 720px;
    border-radius: 46% 46% 8% 8% / 30% 30% 4% 4%;
    background: linear-gradient(180deg, rgba(214,180,170,.55) 0%, rgba(190,160,160,.5) 35%, rgba(40,48,80,.75) 60%, rgba(22,34,60,.6) 85%, rgba(22,34,60,0) 100%);
  }
  .kicker {
    position: absolute;
    top: 44px;
    width: 100%;
    text-align: center;
    font-family: "Montserrat", sans-serif;
    font-weight: 800;
    font-size: 27px;
    color: var(--slate);
    letter-spacing: -0.3px;
  }
  .headliner {
    position: absolute;
    top: 66px;
    width: 100%;
    text-align: center;
    font-family: "Montserrat", sans-serif;
    font-weight: 900;
    font-size: 86px;
    line-height: 1.1;
    letter-spacing: -1px;
    background: linear-gradient(180deg, var(--steel-light) 0%, #c3c9cd 45%, var(--steel-dark) 55%, #6c747a 100%);
    -webkit-background-clip: text;
    background-clip: text;
    color: transparent;
  }
  .presents {
    position: absolute;
    top: 165px;
    width: 100%;
    text-align: center;
    font-family: "Montserrat", sans-serif;
    font-weight: 300;
    font-size: 18px;
    letter-spacing: 27px;
    padding-left: 27px;
    color: #222;
  }
  .ornament {
    position: absolute;
    background: radial-gradient(ellipse 50% 50% at 50% 50%, rgba(var(--ornament-blue), .9) 0%, rgba(var(--ornament-blue), .55) 45%, rgba(var(--ornament-blue), 0) 100%);
  }
  .ornament--crown { left: 256px; top: 918px; width: 416px; height: 20px; }
  .ornament--left { left: 36px; top: 1034px; width: 252px; height: 52px; }
  .ornament--right { left: 646px; top: 1034px; width: 252px; height: 52px; }
  .show-title {
    position: absolute;
    top: 952px;
    width: 100%;
    text-align: center;
    white-space: nowrap;
    font-family: "Cinzel", serif;
    font-weight: 600;
    font-size: 54px;
    line-height: 1;
    letter-spacing: -1px;
    color: #eef1f4;
    text-shadow: 0 2px 3px rgba(0,0,0,.6);
  }
  .show-title .minor { font-size: 36px; }
  .event-date {
    position: absolute;
    top: 1034px;
    width: 100%;
    text-align: center;
    font-weight: 300;
    font-size: 31px;
    line-height: 1.1;
  }
  .divider {
    position: absolute;
    left: 240px;
    top: 1084px;
    width: 480px;
    border-top: 2px dotted rgba(255,255,255,.35);
  }
  .event-details {
    position: absolute;
    top: 1100px;
    width: 100%;
    text-align: center;
    font-weight: 300;
    font-size: 22px;
    line-height: 28px;
  }
</style>
</head>
<body>
<main class="poster">
  <div class="cloud-light"></div>
  <div class="portrait" role="img" aria-label="Portrait photograph of the medium in a dark suit, reaching a hand towards the viewer amid rays of light"></div>

  <p class="kicker">RENOWNED SPIRITUALIST MEDIUM</p>
  <h1 class="headliner">DEWI CARLOW</h1>
  <p class="presents">PRESENTS</p>

  <div class="ornament ornament--crown" role="img" aria-label="Blue decorative scroll flourish"></div>
  <h2 class="show-title">Whispers <span class="minor">from the</span> Lantern</h2>
  <div class="ornament ornament--left" role="img" aria-label="Blue decorative scroll flourish"></div>
  <div class="ornament ornament--right" role="img" aria-label="Blue decorative scroll flourish"></div>
  <p class="event-date">FEB. 3, 2016 AT 6PM</p>
  <div class="divider"></div>
  <p class="event-details">VENUE NAME - 1234 STREET NAME, CITY POSTAL CODE<br>FOR TICKETS CALL 02 1234 5678</p>
</main>
</body>
</html>
```